Business school needs a web design

Who We are:
KRVT is a small business school that offers programs in Project Management. The school is based in West Africa and welcomes students from the whole area. Our aim is to become one of the reference business schools in Africa.

Project Brief:
The site will include all informations relevant for different types of visitors that we have: actual and future students, companies, mass media, future employees, ect. It will present information about subscription, list of programs, presentation of the school and its team,etc.

What We want:
This competition is for Design only no coding! We need design for two pages.
We did some wireframing for the home page and the list of programs page. We made them just to show how we imagine the website would look like. But we encourage creative designs, so you don't have to stick to the wireframe models.

Sites We like:
http://www.ravenmoorcollege.example/
http://www.belvantis.example/fr/etudes.html
http://www.qtl.example/mba/Pages/default.aspx

Color schemes
The logo of the school is red and black. So the color scheme of the website should match that. For the rest, it is opened to your imagination.
Updates

The payment for the project is now garanteed. Good luck to you all !

Target Market(s)

The target market is diversified because we have students of different ages, also company representatives or employees that might visit the website for recruitment purposes. But the majority of our audience should be aged between 20 - 30 years.

Industry/Entity Type

Small Business

Requirements
Must have
• The design must include two pages: a home page and another interior page : might be the list of programs or any other page relevant to the domain. The Home page must include a slide show at the beginning.
The background page must be white.
Nice to have
• The use of flat design for this project is preferred.
The use of Pelican scaffold as a base for the design is an asset.

```html
<!DOCTYPE html>
<html lang="fr">
<head>
<meta charset="utf-8">
<title>KRVT – Programmes et Formations</title>
<link rel="stylesheet" href="https://fonts.googleapis.com/css2?family=Open+Sans:wght@300;400;600;700&display=swap">
<style>
  :root{
    --red:#e2231a;
    --ink:#1a1a1a;
    --text:#555;
    --muted:#8a8a8a;
    --line:#d9d9d9;
    --footer:#2b2b2b;
    --footer-deep:#1f1f1f;
    --footer-text:#9a9a9a;
    --white:#fff;
  }
  *{box-sizing:border-box;margin:0;padding:0}
  html,body{width:846px;height:1200px;overflow:hidden;background:var(--white)}
  body{position:relative;font-family:"Open Sans",Arial,sans-serif;color:var(--text)}
  .abs{position:absolute}

  /* header */
  .brand{left:44px;top:30px;display:flex;align-items:center;gap:8px}
  .brand-dot{width:22px;height:22px;background:var(--ink);border-radius:50%}
  .brand-name{font-size:26px;font-weight:700;color:var(--red);letter-spacing:1px}
  .socialize{left:634px;top:14px;font-size:7.5px;color:var(--muted);letter-spacing:.3px}
  .social-top{left:719px;top:9px;display:flex;gap:6px}
  .social-top span{width:20px;height:20px;border-radius:50%;display:block}
  .crumbs{left:463px;top:43px;font-size:7.5px;color:var(--muted)}
  .crumbs b{font-weight:400;margin:0 4px}
  .search{left:670px;top:38px;width:118px;height:18px;border:1px solid var(--line);border-radius:9px;font-size:7.5px;color:#aaa;padding:4px 0 0 10px}
  .search svg{position:absolute;right:6px;top:4px}
  .nav{left:284px;top:72px;display:flex;font-size:9px;color:#444;white-space:nowrap}
  .nav li{list-style:none;display:flex;align-items:center}
  .nav li+li::before{content:"";width:3px;height:3px;background:var(--red);border-radius:50%;margin:0 7px 0 7px}
  .nav .active{color:var(--red)}

  /* hero */
  .hero{left:0;top:101px;width:846px;height:303px;background:linear-gradient(90deg,#8c8580 0%,#b9aea4 35%,#d8cfc4 60%,#a59888 100%)}
  .hero-card{left:29px;top:172px;width:317px;height:182px;background:rgba(20,20,20,.82);color:var(--white);padding:6px 15px}
  .hero-kicker{font-size:28px;font-weight:300;line-height:34px}
  .hero-title{font-size:55px;font-weight:300;line-height:60px;letter-spacing:-1px}
  .hero-text{font-size:11.3px;line-height:16px;font-weight:300;margin-top:6px;white-space:nowrap}
  .btn{display:inline-block;margin-top:9px;background:var(--red);color:var(--white);font-size:11px;font-weight:600;padding:4px 10px}
  .dots{left:409px;top:387px;display:flex;gap:5px}
  .dots i{width:6px;height:6px;border-radius:50%;background:var(--red);display:block}
  .dots i.off{background:var(--white)}

  /* programmes */
  .section-title{font-size:19px;font-weight:300;color:var(--red)}
  .intro{left:0;top:462px;width:846px;text-align:center;font-size:10.5px;line-height:17px;color:var(--muted);font-weight:300}
  .card-title{font-size:11.5px;color:var(--red);font-weight:400}
  .video{width:190px;height:116px;background:linear-gradient(135deg,#8d8a86,#5c5853);border:2px solid #222}
  .video .play{position:absolute;left:82px;top:42px}
  .video .bar{position:absolute;left:0;bottom:0;width:100%;height:13px;background:#1b1b1b}
  .video .bar i{position:absolute;left:10px;top:6px;width:75px;height:2px;background:var(--red)}
  .video .bar em{position:absolute;left:85px;top:6px;width:40px;height:2px;background:#555}
  .meta-title{font-size:9.2px;color:var(--red)}
  .meta-sub{font-size:6px;color:var(--red);text-decoration:underline}
  .meta-views{font-size:7.2px;color:var(--muted)}

  .offer-img{width:89px;height:72px}
  .offer h4{font-size:9.2px;font-weight:400;color:var(--red)}
  .offer .sub{font-size:6px;color:var(--red);text-decoration:underline}
  .offer p{font-size:9px;line-height:18px;color:var(--muted);margin-top:1px}

  /* side share */
  .share{left:811px;top:532px;width:35px}
  .share span{display:flex;align-items:center;justify-content:center;height:31px;margin-bottom:1px;background:#111}
  .share span:nth-child(2),.share span:nth-child(4){background:#2e2e2e}

  /* footer */
  .footer{left:0;top:984px;width:846px;height:167px;background:var(--footer)}
  .footer-bottom{left:0;top:1151px;width:846px;height:49px;background:var(--footer-deep)}
  .f-head{font-size:11px;color:#e8e8e8;font-weight:400}
  .f-list{font-size:6.2px;line-height:12px;color:var(--footer-text);list-style:none}
  .f-time{font-size:5.5px;color:#ddd}
  .date{width:18px;text-align:center}
  .date b{display:block;background:var(--white);color:var(--red);font-size:8px;height:15px;line-height:15px}
  .date i{display:block;background:var(--red);color:var(--white);font-size:6px;font-style:normal;height:9px;line-height:9px}
  .news-lead{font-size:7.2px;line-height:11px;color:#eee}
  .news-text{font-size:6.5px;line-height:12px;color:var(--footer-text)}
  .news-text b{color:#fff;font-weight:400}
  .contact{font-size:6.2px;line-height:16px;color:var(--footer-text)}
  .contact strong{color:#ccc;font-weight:600}
  .copyright{left:63px;top:1173px;font-size:6.5px;color:var(--footer-text)}
  .follow{left:742px;top:1158px;font-size:9.5px;color:#ddd}
  .follow-icons{left:739px;top:1175px;display:flex;gap:4px}
  .follow-icons span{width:15px;height:15px;border-radius:50%;background:#444;display:block}
</style>
</head>
<body>

<header>
  <div class="abs brand"><span class="brand-dot"></span><span class="brand-name">KRVT</span></div>
  <div class="abs socialize">SOCIALIZE WITH US :</div>
  <div class="abs social-top" aria-label="Réseaux sociaux">
    <span style="background:#2fa9e0"></span><span style="background:#d6333b"></span><span style="background:#4a6ea9"></span>
  </div>
  <div class="abs crumbs">REPERTOIRE DU PERSONAL<b>›</b>BLOGUE<b>›</b>SALLE DE PARSE</div>
  <div class="abs search">SEARCH...
    <svg width="9" height="9" viewBox="0 0 10 10"><circle cx="4" cy="4" r="3" fill="none" stroke="#aaa" stroke-width="1.2"/><line x1="6.2" y1="6.2" x2="9" y2="9" stroke="#aaa" stroke-width="1.2"/></svg>
  </div>
  <ul class="abs nav">
    <li class="active">A PROPOS DE L'KRVT</li>
    <li>PROGRAMMES ET FORMATIONS</li>
    <li>ETUDIANTS</li>
    <li>NOVELLES ET EVENMENTS</li>
    <li>ENTERPRISES</li>
  </ul>
</header>

<section>
  <div class="abs hero" role="img" aria-label="Étudiante souriante tenant une tablette dans une salle de cours"></div>
  <div class="abs hero-card">
    <div class="hero-kicker">Etu diianst</div>
    <div class="hero-title">Fornations</div>
    <p class="hero-text">Lorem ipsum dolor sit amet, consectetur adipiscing elit.<br>Fusce elementum, nulla vel pellentesque consequat,</p>
    <span class="btn">Lire la Suite</span>
  </div>
  <div class="abs dots"><i></i><i></i><i class="off"></i></div>
</section>

<section>
  <h2 class="abs section-title" style="left:0;top:430px;width:846px;text-align:center">PROGRAMMES ET FORMATION</h2>
  <p class="abs intro">Lorem ipsum dolor sit amet, consectetur adipisicing elit, sed do eiusmod tempor incididunt ut labore et dolore<br>magna aliqua. Ut enim ad minim veniam, quis nostrud exercitation ullamco laboris nisi ut aliquip ex ea commodo</p>

  <h3 class="abs card-title" style="left:64px;top:531px">Formation Diplomants</h3>
  <h3 class="abs card-title" style="left:318px;top:530px">Certificate Professionals</h3>
  <h3 class="abs card-title" style="left:578px;top:530px">Formations a la carte</h3>

  <div class="abs video" style="left:65px;top:558px" role="img" aria-label="Vidéo : deux étudiants travaillant ensemble"><svg class="play" width="22" height="22" viewBox="0 0 22 22"><polygon points="5,2 20,11 5,20" fill="rgba(255,255,255,.7)"/></svg><div class="bar"><i></i><em></em></div></div>
  <div class="abs video" style="left:321px;top:558px" role="img" aria-label="Vidéo : deux étudiants travaillant ensemble"><svg class="play" width="22" height="22" viewBox="0 0 22 22"><polygon points="5,2 20,11 5,20" fill="rgba(255,255,255,.7)"/></svg><div class="bar"><i></i><em></em></div></div>
  <div class="abs video" style="left:579px;top:558px" role="img" aria-label="Vidéo : deux étudiants travaillant ensemble"><svg class="play" width="22" height="22" viewBox="0 0 22 22"><polygon points="5,2 20,11 5,20" fill="rgba(255,255,255,.7)"/></svg><div class="bar"><i></i><em></em></div></div>

  <div class="abs" style="left:64px;top:689px"><div class="meta-title">Lorem Ipsum Dolor Sit Amet</div><div class="meta-sub">Title</div><div class="meta-views">221,996 views 1 day ago</div></div>
  <div class="abs" style="left:322px;top:689px"><div class="meta-title">Lorem Ipsum Dolor Sit Amet</div><div class="meta-sub">Title</div><div class="meta-views">221,996 views 1 day ago</div></div>
  <div class="abs" style="left:581px;top:689px"><div class="meta-title">Lorem Ipsum Dolor Sit Amet</div><div class="meta-sub">Title</div><div class="meta-views">221,996 views 1 day ago</div></div>
</section>

<section>
  <h2 class="abs section-title" style="left:64px;top:755px">PROGRAMMES OFFERTS</h2>

  <div class="abs offer-img" style="left:63px;top:793px;background:linear-gradient(135deg,#c9a48a,#5a4a42)" role="img" aria-label="Étudiantes souriantes en groupe"></div>
  <div class="abs offer" style="left:163px;top:791px"><h4>Lorem Ipsum Dolor Sit Amet</h4><div class="sub">Title</div><p>Lorem ipsum dolor sit amet, consectetur<br>adipisicing elit, sed do eiusmod tempor</p></div>

  <div class="abs offer-img" style="left:413px;top:793px;background:linear-gradient(135deg,#e8e6e3,#7c7a80)" role="img" aria-label="Mains prenant des notes en réunion"></div>
  <div class="abs offer" style="left:513px;top:791px"><h4>Lorem Ipsum Dolor Sit Amet</h4><div class="sub">Title</div><p>Lorem ipsum dolor sit amet, consectetur<br>adipisicing elit, sed do eiusmod tempor</p></div>

  <div class="abs offer-img" style="left:63px;top:882px;background:linear-gradient(180deg,#9a9690,#ece9e4)" role="img" aria-label="Vidéoprojecteur sur une table"></div>
  <div class="abs offer" style="left:163px;top:880px"><h4>Lorem Ipsum Dolor Sit Amet</h4><div class="sub">Title</div><p>Lorem ipsum dolor sit amet, consectetur<br>adipisicing elit, sed do eiusmod tempor</p></div>

  <div class="abs offer-img" style="left:413px;top:882px;background:linear-gradient(135deg,#b8a696,#e4e0da)" role="img" aria-label="Deux étudiants lisant un document"></div>
  <div class="abs offer" style="left:513px;top:880px"><h4>Lorem Ipsum Dolor Sit Amet</h4><div class="sub">Title</div><p>Lorem ipsum dolor sit amet, consectetur<br>adipisicing elit, sed do eiusmod tempor</p></div>
</section>

<aside class="abs share" aria-label="Partager">
  <span></span><span></span><span></span>
  <span><svg width="18" height="14" viewBox="0 0 18 14"><ellipse cx="9" cy="6" rx="8" ry="5.5" fill="#fff"/><polygon points="4,10 3,14 8,11" fill="#fff"/></svg></span>
  <span><svg width="16" height="14" viewBox="0 0 16 14"><rect x="4" y="0" width="8" height="4" fill="#fff"/><rect x="0" y="4" width="16" height="6" rx="1" fill="#fff"/><rect x="4" y="8" width="8" height="6" fill="#fff" stroke="#111"/></svg></span>
</aside>

<footer>
  <div class="abs footer"></div>

  <h4 class="abs f-head" style="left:66px;top:1013px">Latest News</h4>
  <div class="abs date" style="left:67px;top:1037px"><b>15</b><i>Jan</i></div>
  <p class="abs news-lead" style="left:91px;top:1035px">Lorem ipsum dolor sit<br>amet, consectetur<br>adipiscing elit.</p>
  <p class="abs news-text" style="left:67px;top:1073px">Lorem ipsum dolor sit amet, consectetur<br>adipiscing elit. Donec hendrerit vehicula<br>est, in consequat libero. <b>read more</b></p>

  <h4 class="abs f-head" style="left:263px;top:1013px">A propos</h4>
  <ul class="abs f-list" style="left:263px;top:1035px"><li>Apro De iskrvt</li><li>Admission</li><li>Colendrier</li></ul>
  <div class="abs f-time" style="left:264px;top:1076px">10 hours ago</div>

  <h4 class="abs f-head" style="left:378px;top:1014px">Nosprise</h4>
  <ul class="abs f-list" style="left:380px;top:1035px"><li>Collection Management</li><li>Campaign Tracker</li><li>Document Capture</li><li>SheetReports</li><li>Loyalty</li><li>PDF-2-LEDGER</li><li>Docs</li><li>EDIFLOW</li></ul>
  <div class="abs f-time" style="left:380px;top:1130px">10 hours ago</div>

  <h4 class="abs f-head" style="left:521px;top:1013px">Etudiants</h4>
  <ul class="abs f-list" style="left:522px;top:1034px"><li>Accueil</li><li>Webshop B2C</li></ul>
  <h4 class="abs f-head" style="left:521px;top:1063px">KRVT</h4>
  <div class="abs contact" style="left:522px;top:1080px">
    <div><svg width="5" height="6" viewBox="0 0 6 8"><path d="M3 0a3 3 0 0 1 3 3c0 2-3 5-3 5S0 5 0 3a3 3 0 0 1 3-3z" fill="#999"/></svg> <strong>Address:</strong> 1234 Street Name,</div>
    <div><svg width="5" height="6" viewBox="0 0 6 8"><path d="M1 0h2l1 2-1 1 2 2 1-1 0 2-2 1C2 7 0 4 0 2z" fill="#999"/></svg> <strong>Phone:</strong> (123) 456-7890</div>
    <div><svg width="6" height="5" viewBox="0 0 8 6"><rect x=".5" y=".5" width="7" height="5" fill="none" stroke="#999"/><path d="M.5 .5 4 3.5 7.5.5" fill="none" stroke="#999"/></svg> <strong>Email:</strong> <span style="color:#fff">mail@example.com</span></div>
  </div>

  <h4 class="abs f-head" style="left:717px;top:1014px">Enter Prise</h4>
  <ul class="abs f-list" style="left:719px;top:1035px"><li>Collection Management</li><li>Campaign Tracker</li><li>Document Capture</li><li>SheetReports</li><li>Loyalty</li><li>PDF-2-LEDGER</li><li>Docs</li><li>EDIFLOW</li></ul>
  <div class="abs f-time" style="left:719px;top:1129px">10 hours ago</div>

  <div class="abs footer-bottom"></div>
  <div class="abs copyright">© Copyright 2013 by. All Rights Reserved.</div>
  <div class="abs follow">Follow Us</div>
  <div class="abs follow-icons" aria-label="Suivez-nous"><span></span><span></span><span></span></div>
</footer>

</body>
</html>
```